Renewable Energy company needs a new website

We are renewable energy company that has been operating for 3 years now and require a new website design. We are looking to upgrade our website to be comparable to our competitors. We are not a brick and mortar business so our website does need to be very appealing and convey a sense of authenticity and trust to the consumer. It will also heavily display our current system special and offering etc. The final design needs to be visually appealing in a marketing sense however also needs to convey a high sense of professionalism.

Target Market(s)

Consumers of solar systems for installation on their home or business.

Coding

Coded - Design and coding required

Number of Pages Required

3 page

Font styles to use
Sans Serif

Colors

Designer to choose colors to be used in the design.

Requirements
Must have
• A home page, a page for residential solar systems including the packages we are currently offering and a commercial page for larger installations of solar systems.
• www.torvapower.com.au
Nice to have
• As a template we do like this https://www.bluneklight.com.au/qld/ in terms of design elements and layout of the page.

```html
<!DOCTYPE html>
<html lang="en">
<head>
<meta charset="utf-8">
<title>Torva Power — Go Solar &amp; Grow Your Business</title>
<link rel="stylesheet" href="https://fonts.googleapis.com/css2?family=Poppins:wght@400;500;600&family=Open+Sans:wght@400;600;700&display=swap">
<style>
:root{
  --red:#c8202f;
  --ink:#1d1d1f;
  --text:#555;
  --muted:#888;
  --soft:#f1f1f3;
  --footer:#222223;
  --sky-a:#4d8fbf;
  --sky-b:#f28a73;
  --panel-a:#1f3e7a;
  --panel-b:#5b7fbf;
  --badge:#e3e3e6;
}
*{box-sizing:border-box;margin:0;padding:0}
html,body{width:1200px;height:4418px;overflow:hidden;background:#fff}
body{position:relative;font-family:"Open Sans",sans-serif;color:var(--ink)}
.abs{position:absolute}
.photo{position:absolute;display:block}
h1,h2,h3,h4{font-family:"Poppins",sans-serif;font-weight:500}

/* header */
.site-header{position:absolute;left:0;top:0;width:1200px;height:82px;background:#fff}
.brand-name{position:absolute;font-family:"Poppins",sans-serif;font-weight:600;font-size:20px;line-height:1;color:var(--ink);letter-spacing:.2px}
.site-header .brand-name{left:149px;top:31px}
.nav{position:absolute;left:449px;top:36px;display:flex;gap:22px;font-family:"Poppins",sans-serif;font-size:9px;font-weight:600;color:#333;letter-spacing:.4px}

/* hero */
.hero{position:absolute;left:0;top:82px;width:1200px;height:621px;overflow:hidden}
.hero .photo{left:0;top:0;width:1200px;height:621px;background:linear-gradient(180deg,rgba(0,0,0,0) 0%,rgba(0,0,0,0) 55%,var(--panel-a) 62%,var(--panel-b) 80%,#c9b8a8 92%),linear-gradient(100deg,var(--sky-a) 0%,#b0a8c4 45%,var(--sky-b) 100%)}
.hero-title{position:absolute;left:0;width:1200px;top:226px;text-align:center;font-size:31px;color:#1b1b1b}
.hero-badge{position:absolute;left:487px;top:283px;width:224px;height:28px;background:var(--red);color:#fff;font-family:"Poppins",sans-serif;font-size:12px;text-align:center;line-height:28px}
.hero-wave{position:absolute;left:0;bottom:0}

/* intro */
.intro-title{left:274px;top:748px;font-size:24px;line-height:31px;color:#111}
.intro-copy{left:274px;top:823px;width:352px;font-size:10px;line-height:17px;color:var(--text)}
.pill{position:absolute;background:var(--red);color:#fff;font-family:"Poppins",sans-serif;font-size:11px;border-radius:16px;display:flex;align-items:center;justify-content:center;gap:10px}
.pill .arrow{width:28px;height:1px;background:#fff;position:relative}
.pill .arrow::after{content:"";position:absolute;right:0;top:-3px;width:6px;height:6px;border-top:1px solid #fff;border-right:1px solid #fff;transform:rotate(45deg)}
.dots{left:0;top:917px;width:210px;height:120px;background-image:radial-gradient(#d6d6d6 1px,transparent 1.4px);background-size:7px 7px}
.offer{left:674px;top:711px;width:252px;height:305px;background:var(--red);overflow:hidden}
.offer h3{position:absolute;left:28px;top:72px;color:#fff;font-size:17px;line-height:21px;font-weight:400}
.offer .link{position:absolute;left:30px;top:126px;color:#fff;font-size:8px;font-weight:700;letter-spacing:.8px;border-bottom:1px solid #fff;padding-bottom:2px}
.offer .photo{left:0;top:150px;width:252px;height:155px;background:linear-gradient(160deg,var(--panel-b),var(--panel-a))}

/* segment tiles */
.tile{top:1047px;width:600px;height:355px}
.tile .photo{left:0;top:0;width:600px;height:355px}
.tile-label{position:absolute;left:77px;top:255px;color:#fff;font-family:"Poppins",sans-serif;font-weight:600;font-size:27px;line-height:33px}

/* features */
.feat{position:absolute;width:190px}
.feat h4{font-size:14px;line-height:21px;color:#111;margin-bottom:6px}
.feat p{font-size:9.5px;line-height:16px;color:var(--text)}
.node{position:absolute;width:64px;height:64px;border:1.5px solid var(--red);border-radius:50%;background:#fff;display:flex;align-items:center;justify-content:center}
.node-label{position:absolute;width:120px;text-align:center;font-size:11px;line-height:14px;color:#222}
.dot{position:absolute;width:16px;height:16px;border-radius:50%;background:var(--red);box-shadow:0 0 0 5px rgba(200,32,47,.15)}

.growth{left:254px;top:2126px;font-size:29px;line-height:36px;color:#111}
.outline-btn{position:absolute;left:790px;top:2168px;width:165px;height:31px;border:1.5px solid var(--red);color:var(--red);font-size:8.5px;font-weight:700;letter-spacing:1px;display:flex;align-items:center;justify-content:center}

/* gallery */
.gallery .photo{top:2242px;width:240px;height:264px}

/* products */
.products-title{left:0;width:1200px;top:2552px;text-align:center;font-size:20px;color:#111}
.products-sub{left:0;width:1200px;top:2588px;text-align:center;font-size:11px;color:#333}
.product{position:absolute;top:2726px;width:170px;text-align:center}
.product .photo{position:relative;margin:0 auto;width:120px;height:105px}
.product span{display:block;margin-top:18px;font-size:11px;line-height:15px;color:#333}

/* info cards */
.card{position:absolute;top:2949px;width:347px;height:248px;padding:56px 30px 0}
.card h3{font-size:17px;line-height:24px;color:#222;margin-bottom:16px;font-weight:400}
.card p{font-size:9px;line-height:16px;color:var(--muted)}
.card-outline{left:242px;border:2px solid #222}
.card-soft{left:608px;background:var(--soft)}
.card-soft h3{color:var(--red)}

/* testimonial */
.testimonial-photo{left:0;top:3262px;width:783px;height:302px;background:linear-gradient(180deg,#a8b8c8 0%,#8ea2b8 40%,#2e4f86 60%,#1c3466 100%)}
.testimonial-red{left:783px;top:3262px;width:417px;height:302px;background:var(--red)}
.eyebrow{left:304px;top:3386px;color:#fff;font-size:8px;font-weight:700;letter-spacing:1.4px}
.testimonial-heading{left:304px;top:3404px;color:#fff;font-size:24px;line-height:30px}
.quote-card{left:608px;top:3322px;width:287px;height:177px;background:#fff;padding:60px 34px 0}
.quote-card p{font-style:italic;font-size:11px;line-height:17px;color:#333}
.quote-card .who{margin-top:12px;font-size:9px;font-weight:700;font-style:normal;color:#111}
.quote-mark{left:634px;top:3290px}

/* partners */
.partners-title{left:237px;top:3658px;font-size:18px;color:#111}
.partners-rule{left:415px;top:3614px;width:2px;height:108px;background:#222}
.badge{position:absolute;top:3650px;width:100px;height:42px;background:var(--badge);border-radius:4px}

/* quote form */
.quote-bg{left:0;top:3752px;width:1200px;height:422px;background:#ededee}
.quote-photo{left:669px;top:3752px;width:531px;height:422px;background:linear-gradient(160deg,#cfe0ee 0%,#8fb3d3 35%,#3b5f96 60%,#1e355f 100%)}
.quote-title{left:264px;top:3904px;font-size:20px;line-height:25px;color:#111}
.quote-copy{left:264px;top:3960px;font-size:12px;line-height:21px;color:#222}
.form{left:528px;top:3771px;width:305px;height:386px;background:#fff;padding:20px 30px}
.field{height:28px;border:1px solid #e2e2e2;margin-bottom:9px;font-size:8px;color:#777;padding:9px 12px}
.field.msg{height:72px}
.submit{height:30px;background:var(--red);color:#fff;font-size:8.5px;font-weight:600;text-align:center;line-height:30px}

/* footer */
.site-footer{left:0;top:4174px;width:1200px;height:244px;background:var(--footer)}
.site-footer-brand{left:271px;top:4264px;color:#fff}
.f-col{position:absolute;top:4262px}
.f-col h4{display:flex;align-items:center;gap:6px;font-family:"Poppins",sans-serif;color:#fff;font-size:13px;font-weight:400;margin-bottom:6px}
.f-col p{font-size:9px;line-height:15px;color:#8a8a8a}
.copyright{left:0;width:1200px;top:4389px;text-align:center;font-size:9px;color:#9a9a9a}
</style>
</head>
<body>

<header class="site-header">
  <div class="brand-name">Torva Power</div>
  <nav class="nav">
    <span>HOME</span><span>ABOUT US</span><span>RESIDENTIAL</span><span>COMMERCIAL</span><span>OFF-GRID</span><span>PRODUCT CATALOG</span><span>OUR PROJECTS</span><span>CONTACT US</span>
  </nav>
</header>

<section class="hero">
  <div class="photo" role="img" aria-label="Wind turbines above rows of solar panels under a sunset sky"></div>
  <h1 class="hero-title">Go Solar &amp; Grow Your Business</h1>
  <div class="hero-badge">Professional Solar Panel Supplier</div>
  <svg class="hero-wave" width="1200" height="150" viewBox="0 0 1200 150" preserveAspectRatio="none">
    <path d="M0 90 C180 160 360 150 560 95 C760 40 940 30 1080 90 C1140 115 1180 130 1200 130 L1200 150 L0 150 Z" fill="#fff"/>
  </svg>
</section>

<h2 class="abs intro-title">Tired of the Power Bill<br>getting larger each year?</h2>
<p class="abs intro-copy">Torva Power is Australia's top provider and authority in solar &amp; off-grid energy solutions. We're here to help you save up to 80% on your energy costs through our effective and efficient energy management systems!</p>
<div class="pill" style="left:274px;top:917px;width:186px;height:30px">Read more about us <span class="arrow"></span></div>
<div class="abs dots"></div>
<div class="abs offer">
  <h3>Businesses Cut<br>80% Off Their Power Bill</h3>
  <span class="link">REQUEST FOR FREE QUOTE</span>
  <div class="photo" role="img" aria-label="Close view of a blue solar panel array"></div>
</div>

<div class="abs tile" style="left:0">
  <div class="photo" role="img" aria-label="Solar panels mounted on a residential home roof" style="background:linear-gradient(160deg,#9ab4c9 0%,#6f7f86 30%,#2a3f6e 55%,#1e2e52 80%,#8a7a62 100%)"></div>
  <div class="tile-label">Solar for<br>Residential</div>
</div>
<div class="abs tile" style="left:600px">
  <div class="photo" role="img" aria-label="Large solar array on a commercial building rooftop" style="background:linear-gradient(170deg,#8aa6c4 0%,#44623c 22%,#2b4478 40%,#3a5a94 70%,#c9ccd2 100%)"></div>
  <div class="tile-label">Solar for<br>Commercial</div>
</div>

<svg class="abs" style="left:0;top:1402px" width="1200" height="720">
  <g stroke="#cfcfcf" stroke-width="1" fill="none">
    <line x1="595" y1="182" x2="595" y2="258"/>
    <line x1="595" y1="325" x2="595" y2="402"/>
    <line x1="595" y1="470" x2="595" y2="548"/>
    <polyline points="458,124 500,200 530,200"/>
    <polyline points="730,263 690,338 660,338"/>
    <polyline points="458,413 500,488 530,488"/>
    <polyline points="730,558 690,632 660,632"/>
  </g>
</svg>
<div class="dot" style="left:450px;top:1518px"></div>
<div class="dot" style="left:722px;top:1657px"></div>
<div class="dot" style="left:450px;top:1807px"></div>
<div class="dot" style="left:722px;top:1953px"></div>

<div class="node" style="left:563px;top:1518px"><svg width="30" height="30" viewBox="0 0 30 30" fill="none" stroke="#c8202f" stroke-width="1.4"><path d="M16 5 L10 16 H15 L13 25 L20 13 H15 Z"/><path d="M4 15 H7 M23 15 H26 M6 6 L8 8 M24 6 L22 8"/></svg></div>
<div class="node-label" style="left:535px;top:1591px">Commercial<br>Solar Power</div>
<div class="node" style="left:563px;top:1662px"><svg width="30" height="30" viewBox="0 0 30 30" fill="none" stroke="#c8202f" stroke-width="1.4"><path d="M11 3 V9 M19 3 V9 M8 9 H22 V13 A7 7 0 0 1 8 13 Z"/><path d="M15 19 C12 23 12 26 15 27 C18 26 18 23 15 19 Z"/></svg></div>
<div class="node-label" style="left:535px;top:1733px">Solar<br>Water Pumps</div>
<div class="node" style="left:563px;top:1807px"><svg width="30" height="30" viewBox="0 0 30 30" fill="none" stroke="#c8202f" stroke-width="1.4"><circle cx="15" cy="10" r="4"/><path d="M15 2 V4 M15 16 V18 M7 10 H9 M21 10 H23 M9 4 L10.5 5.5 M21 4 L19.5 5.5"/><path d="M4 25 L8 20 H24 L26 25 Z M10 20 L9 25 M15 20 V25 M20 20 L21 25"/></svg></div>
<div class="node-label" style="left:535px;top:1880px">Off Grid<br>Power</div>
<div class="node" style="left:563px;top:1953px"><svg width="30" height="30" viewBox="0 0 30 30" fill="none" stroke="#c8202f" stroke-width="1.4"><path d="M5 15 L15 6 L25 15 M8 13 V25 H22 V13"/><circle cx="15" cy="18" r="2.5"/></svg></div>
<div class="node-label" style="left:535px;top:2025px">Residential<br>Solar Power</div>

<div class="feat" style="left:242px;top:1498px"><h4>Reduce Costs,<br>Grow Your Business</h4><p>If you're running a business, then our Commercial Energy Solutions are perfectly suited for your power-intensive operations!</p></div>
<div class="feat" style="left:771px;top:1600px"><h4>Go Solar, Eliminate<br>Fuel Cost</h4><p>We know you want to grow so we help you find more cost-efficient alternatives versus expensive traditional options such as fossil fuel water pumps.</p></div>
<div class="feat" style="left:242px;top:1751px"><h4>Avoid Blackouts,<br>Go Off-Grid</h4><p>In a country where blackouts and power outages are all too common, our Off-Grid Power Solutions can make your electricity more dependable to avoid disruption in your operations.</p></div>
<div class="feat" style="left:771px;top:1889px"><h4>Save Money<br>For Your Family</h4><p>In a country where blackouts and power outages are all too common, our Off-Grid Power Solutions can make your electricity more dependable to avoid disruption in your operations.</p></div>

<h2 class="abs growth">Experience genuine<br>substantial business growth.</h2>
<div class="outline-btn">VIEW ALL &nbsp;OUR PROJECTS</div>

<div class="gallery">
  <div class="photo" role="img" aria-label="Solar panels in front of a city skyline with wind turbines" style="left:0;background:linear-gradient(180deg,#9ec2e6,#5f7e9c 55%,#2f4b7d)"></div>
  <div class="photo" role="img" aria-label="Solar panel field at sunrise" style="left:240px;background:linear-gradient(180deg,#b8d2ea,#f1c98a 40%,#2f4f86 60%,#5b7a3c)"></div>
  <div class="photo" role="img" aria-label="Solar panels on a brick house roof with a wind turbine" style="left:480px;background:linear-gradient(180deg,#a9c3de,#6a7e95 40%,#2a3e6c 65%,#8a4a34)"></div>
  <div class="photo" role="img" aria-label="Wind turbines over a green field" style="left:720px;background:linear-gradient(180deg,#c9d7e6,#dfe6ee 55%,#7e9a55 75%,#5d7a38)"></div>
  <div class="photo" role="img" aria-label="Solar panels on a blue timber house roof" style="left:960px;background:linear-gradient(180deg,#b9d1ea,#2f4b80 45%,#27406f 65%,#3a5a9a)"></div>
</div>

<h2 class="abs products-title">World-leading solar manufacturers products</h2>
<p class="abs products-sub">Your one-stop-shop for solar energy supplies</p>
<div class="pill" style="left:504px;top:2624px;width:185px;height:30px">Explore our products <span class="arrow"></span></div>

<div class="product" style="left:225px"><div class="photo" role="img" aria-label="Integrated PV system on a stand" style="background:linear-gradient(150deg,#fff 20%,#4a78c0 45%,#1f3f7a 70%,#fff 85%)"></div><span>Integrated PV System</span></div>
<div class="product" style="left:400px"><div class="photo" role="img" aria-label="Flexible solar panels" style="background:linear-gradient(150deg,#fff 15%,#1d2d5c 40%,#2c3f78 70%,#fff 85%)"></div><span>Solar Panels</span></div>
<div class="product" style="left:587px"><div class="photo" role="img" aria-label="Folding solar tracker panels" style="background:linear-gradient(150deg,#fff 15%,#2a2f3a 40%,#4a5262 70%,#fff 85%)"></div><span>Solar Trackers</span></div>
<div class="product" style="left:789px"><div class="photo" role="img" aria-label="Rooftop mounting system with green pole" style="background:linear-gradient(90deg,#fff 10%,#3b7fe0 15%,#3b7fe0 65%,#7dc243 72%,#fff 80%)"></div><span>Mounting Systems rooftop<br>structures</span></div>

<div class="card card-outline">
  <h3>A More Cost-Efficient Alternative<br>To Your Irrigation Needs</h3>
  <p>Conventional water pump systems can be quite costly. Volatile prices of fuel and other related expenses contribute to adding massive burden to your operations. Torva Power offers you a more cost-efficient alternative through our solar water pumps. Now, increasing your efficiency while reducing your costs is possible!</p>
</div>
<div class="card card-soft">
  <h3>Add Thousands of<br>Dollars to Your Bottomline</h3>
  <p>Torva Power has a full range of energy management solutions that will help your business reduce energy costs. In addition, we will also help you in maximising your available tax deductions while shortening your payback period. The overall result? Thousands of dollars added to your bottomline!</p>
</div>

<div class="abs testimonial-photo" role="img" aria-label="Technicians installing solar panels on a rooftop"></div>
<div class="abs testimonial-red"></div>
<div class="abs eyebrow">TESTIMONIALS</div>
<h2 class="abs testimonial-heading">Customers About Our<br>Solar Panels</h2>
<div class="abs quote-card">
  <p>Have been a pleasure to deal with and came up with a combinations of ideas to save money</p>
  <p class="who">– DELPHINE</p>
</div>
<svg class="abs quote-mark" width="54" height="42" viewBox="0 0 54 42"><path d="M4 40 C2 22 8 8 22 2 L24 7 C15 11 13 18 13 24 H22 V40 Z M30 40 C28 22 34 8 48 2 L50 7 C41 11 39 18 39 24 H48 V40 Z" fill="none" stroke="#f2b51d" stroke-width="4"/></svg>

<h2 class="abs partners-title">Our Solar Partners</h2>
<div class="abs partners-rule"></div>
<div class="badge" style="left:437px"></div>
<div class="badge" style="left:566px"></div>
<div class="badge" style="left:710px"></div>
<div class="badge" style="left:855px"></div>

<div class="abs quote-bg"></div>
<div class="abs quote-photo" role="img" aria-label="Solar panels on a house roof with a wind turbine against blue sky"></div>
<h2 class="abs quote-title">Free No<br>Obligation Quote!</h2>
<p class="abs quote-copy">Get a FREE customized Quote For<br>your Home or Business!</p>
<form class="abs form">
  <div class="field">Name</div>
  <div class="field">Email Address</div>
  <div class="field">Phone Number</div>
  <div class="field">Postcode</div>
  <div class="field">Commercial</div>
  <div class="field msg">Message</div>
  <div class="submit">Get Free Quote</div>
</form>

<footer class="abs site-footer"></footer>
<div class="brand-name site-footer-brand">Torva Power</div>
<div class="f-col" style="left:528px">
  <h4><svg width="12" height="14" viewBox="0 0 12 14" fill="none" stroke="#fff" stroke-width="1.2"><path d="M6 13 C2 8 1 6 1 5 A5 5 0 0 1 11 5 C11 6 10 8 6 13 Z"/><circle cx="6" cy="5" r="1.7"/></svg>Address</h4>
  <p>48-52 Harlow Road<br>Marsden QLD 4132</p>
</div>
<div class="f-col" style="left:696px">
  <h4><svg width="13" height="13" viewBox="0 0 13 13" fill="none" stroke="#fff" stroke-width="1.2"><path d="M2 1 H5 L6 4 L4 5 C5 7 6 8 8 9 L9 7 L12 8 V11 C12 12 11 12 10 12 C5 11 1 7 1 2 C1 1 1 1 2 1 Z"/></svg>Phone</h4>
  <p>(07)3000 4827</p>
</div>
<div class="f-col" style="left:828px">
  <h4><svg width="13" height="13" viewBox="0 0 13 13" fill="none" stroke="#fff" stroke-width="1.2"><circle cx="6.5" cy="6.5" r="5.5"/><path d="M6.5 3 V6.5 L9 8"/></svg>Open Hours</h4>
  <p>Monday - Friday<br>8:00AM - 5:00PM</p>
</div>
<p class="abs copyright">Copyright 2019 Torva Power. All Rights Reserved.</p>

</body>
</html>
```